Tessel PR (young, fun PR agency) needs a Business Card Design

We need a new business card design that reflects who we are as a company. We're a Sydney-based PR agency that's six years old with clients including Blue Heron, Duneprint, OLVEN, Lou Carvell etc. - just check out our website for more info: www.tesselpr.com.au. We would like to see designs that bring to life our company name and what we do (generating media coverage for brands on TV, radio, online and in newspapers and magazines). We don't want a corporate style card but one that people take notice of and think 'wow that's a cool business card'. It doesn't have to be the standard rectangle shape and can incorporate humour.

Target Market(s)

Clients (generally cool/creative types) and media

Industry/Entity Type

Business

Requirements
Must have
• The card must feature our business logo (which can be updated if you like) and use both sides.
Nice to have
• The card could feature a cool illustration

```html
<!DOCTYPE html>
<html lang="en">
<head>
<meta charset="utf-8">
<title>Tessel PR – Business Card</title>
<link rel="stylesheet" href="https://fonts.googleapis.com/css2?family=Open+Sans:wght@300;400;700&display=swap">
<style>
  :root {
    --backdrop: #3b3b3d;
    --card: #1d1d1f;
    --card-edge: #29292b;
    --orange: #d9801f;
    --orange-deep: #a85a12;
    --orange-light: #e89a3c;
    --paper-white: #f2f2f0;
    --text-light: #e6e6e6;
  }
  * { box-sizing: border-box; margin: 0; padding: 0; }
  html, body {
    width: 1200px;
    height: 900px;
    overflow: hidden;
    background: var(--backdrop);
    font-family: "Open Sans", Arial, sans-serif;
  }
  .stage {
    width: 1200px;
    height: 900px;
    display: flex;
    align-items: center;
    justify-content: center;
  }
  .business-card {
    position: relative;
    width: 440px;
    height: 770px;
    background: linear-gradient(160deg, var(--card-edge), var(--card) 60%);
    overflow: hidden;
    box-shadow: 0 18px 40px rgba(0,0,0,0.45);
  }
  .logo-block {
    position: absolute;
    top: 34px;
    left: 212px;
    width: 196px;
    height: 196px;
    background: linear-gradient(135deg, var(--orange-light), var(--orange) 45%, var(--orange-deep));
  }
  .wordmark {
    position: absolute;
    top: 196px;
    left: 34px;
    font-weight: 700;
    font-size: 66px;
    line-height: 1;
    letter-spacing: -1px;
    color: var(--paper-white);
    text-transform: uppercase;
  }
  .person {
    position: absolute;
    top: 300px;
    left: 36px;
    color: var(--text-light);
  }
  .person-name {
    font-weight: 300;
    font-size: 34px;
    letter-spacing: 0.5px;
    line-height: 1.1;
  }
  .person-title {
    font-weight: 300;
    font-size: 22px;
    margin-top: 2px;
  }
  .accent-bar {
    position: absolute;
    top: 398px;
    left: 36px;
    width: 262px;
    height: 14px;
    background: linear-gradient(90deg, var(--orange-deep), var(--orange-light) 50%, var(--orange-deep));
  }
  .contact {
    position: absolute;
    top: 432px;
    left: 36px;
    list-style: none;
    color: var(--text-light);
    font-weight: 400;
    font-size: 18px;
    line-height: 1.32;
  }
  .contact .address { margin-top: 10px; }
  .footer-block {
    position: absolute;
    left: 40px;
    bottom: 0;
    width: 250px;
    height: 150px;
    background: linear-gradient(135deg, var(--orange-light), var(--orange) 50%, var(--orange-deep));
  }
  .footer-stripe {
    position: absolute;
    left: 0;
    top: 40px;
    width: 150px;
    height: 52px;
    background: var(--paper-white);
  }
</style>
</head>
<body>
  <main class="stage">
    <article class="business-card" aria-label="Tessel PR business card, front">
      <div class="logo-block"></div>
      <div class="wordmark">Tessel PR</div>

      <header class="person">
        <h1 class="person-name">Nadia Corrigan</h1>
        <p class="person-title">Managing Director</p>
      </header>

      <div class="accent-bar"></div>

      <ul class="contact">
        <li class="phone">02 9000 1234</li>
        <li class="web">www.tesselpr.com.au</li>
        <li class="email">nadia@tesselpr.com.au</li>
        <li class="address">Level 2, 41 Kettle Lane,<br>Surry Hills, Sydney 2010</li>
      </ul>

      <div class="footer-block">
        <div class="footer-stripe"></div>
      </div>
    </article>
  </main>
</body>
</html>
```